Brightmoor Dental Care Stationery

create stationery, business cards and envelops for business. Use current logo on website but open to new fonts for the business name. Business name is Brightmoor Dental Care, would like below the name added "Cosmetic - Family - Implants" Website is www.brightmoordentalcareXQ.example. I would like to have modern look, clean, and professional. The water mark of the logo is a great thing to ad as well.

Target Market(s)

General public, Families, Cosmetic, Implant

Industry/Entity Type

Dental

Font styles to use
Sans Serif

Colors
9bcb3c
000000
757575
c9c9c9

Requirements
Must have
• Would like to see different versions of the current logo. Improvements, color, sytle, and class.
Nice to have
• current font has double "oo" in the Brightmoor logo, does not need to have with new logo.

```html
<!DOCTYPE html>
<html lang="en">
<head>
<meta charset="utf-8">
<title>Brightmoor Dental Care – Stationery</title>
<link rel="stylesheet" href="https://fonts.googleapis.com/css2?family=Montserrat:wght@700&family=Roboto:ital,wght@0,300;0,400;1,300&display=swap">
<style>
  :root {
    --green: #9bcb3c;
    --black: #1e1e1e;
    --grey: #757575;
    --grey-light: #c9c9c9;
    --text: #4d4d4d;
    --board-band: #939497;
    --white: #ffffff;
  }
  * { margin: 0; padding: 0; box-sizing: border-box; }
  html, body { width: 1200px; height: 1000px; overflow: hidden; }
  body {
    position: relative;
    font-family: "Roboto", Arial, sans-serif;
    background: radial-gradient(ellipse 75% 60% at 50% 35%, #d6d7d9 0%, #bfc0c3 55%, #a7a8ab 100%);
  }
  .board-band {
    position: absolute; left: 0; top: 797px; width: 1200px; height: 203px;
    background: var(--board-band);
  }
  .board-label {
    position: absolute; right: 34px; top: 888px;
    font-family: "Montserrat", Arial, sans-serif; font-weight: 700;
    font-size: 42px; color: var(--white); letter-spacing: 0.5px;
  }

  /* brand lockup: plain circle + name in one colour, one weight */
  .brand { position: absolute; display: flex; align-items: center; }
  .brand__ring { flex: none; border-radius: 50%; border-style: solid; border-color: var(--green); }
  .brand__name {
    font-family: "Roboto", Arial, sans-serif; font-weight: 300;
    color: var(--grey); line-height: 0.95; white-space: nowrap;
  }
  .brand__name span { display: block; }

  .brand--hero { left: 32px; top: 25px; }
  .brand--hero .brand__ring { width: 172px; height: 172px; border-width: 6px; margin-right: 14px; }
  .brand--hero .brand__name { font-size: 64px; }

  .palette {
    position: absolute; left: 857px; top: 78px; width: 308px; height: 55px;
    display: flex;
  }
  .palette__swatch { flex: 1; }
  .palette__swatch--green { background: var(--green); }
  .palette__swatch--grey { background: var(--grey); }
  .palette__swatch--black { background: var(--black); }
  .palette__label {
    position: absolute; inset: 0; display: flex; align-items: center; justify-content: center;
    color: var(--white); font-size: 24px; font-weight: 300;
  }

  /* envelope */
  .envelope {
    position: absolute; left: 30px; top: 302px; width: 1140px; height: 495px;
    background: var(--white); box-shadow: 0 4px 14px rgba(0,0,0,0.25);
  }
  .envelope .brand { left: 22px; top: 22px; }
  .envelope .brand__ring { width: 84px; height: 84px; border-width: 4px; margin-right: 12px; }
  .envelope .brand__name { font-size: 33px; }
  .envelope__contact {
    position: absolute; left: 22px; top: 390px;
    font-size: 16px; line-height: 25px; color: var(--text);
  }
  .divider { color: var(--green); padding: 0 6px; }
  .stripe { position: absolute; bottom: 0; }
  .stripe--green { background: var(--green); clip-path: polygon(0 0, 100% 0, calc(100% - 8px) 100%, 0 100%); }
  .stripe--grey { background: var(--grey); clip-path: polygon(8px 0, 100% 0, 100% 100%, 0 100%); }
  .envelope .stripe { height: 20px; }
  .envelope .stripe--green { left: 0; width: 582px; }
  .envelope .stripe--grey { left: 577px; right: 0; }

  /* business cards */
  .card {
    position: absolute; left: 673px; width: 413px; height: 236px;
    box-shadow: 0 3px 10px rgba(0,0,0,0.3); overflow: hidden;
  }
  .card--front { top: 272px; background: var(--white); }
  .card--back { top: 526px; background: var(--green); }

  .card--front .brand { left: 15px; top: 14px; }
  .card--front .brand__ring { width: 54px; height: 54px; border-width: 3px; margin-right: 8px; }
  .card--front .brand__name { font-size: 21px; }
  .card__rule { position: absolute; left: 15px; top: 84px; width: 254px; height: 1px; background: var(--green); }
  .card__holder { position: absolute; right: 15px; top: 76px; text-align: right; }
  .card__name { font-size: 16px; color: #111; }
  .card__role { font-size: 14px; font-weight: 300; font-style: italic; color: var(--grey); }
  .card__contact {
    position: absolute; left: 15px; top: 124px;
    font-size: 13px; line-height: 19px; color: var(--text);
  }
  .card__watermark {
    position: absolute; left: 320px; top: 122px; width: 120px; height: 120px;
    border-radius: 50%; border: 5px solid #e3e3e3;
  }
  .card--front .stripe { height: 13px; }
  .card--front .stripe--green { left: 0; width: 222px; }
  .card--front .stripe--grey { left: 217px; right: 0; }

  .card--back .brand { left: 85px; top: 79px; }
  .card--back .brand__ring { width: 78px; height: 78px; border-width: 3px; border-color: var(--black); margin-right: 10px; }
  .card--back .brand__name { font-size: 29px; color: var(--black); }
</style>
</head>
<body>
  <div class="brand brand--hero">
    <div class="brand__ring"></div>
    <div class="brand__name"><span>BRIGHTMOOR</span><span>dental care</span></div>
  </div>

  <div class="palette">
    <div class="palette__swatch palette__swatch--green"></div>
    <div class="palette__swatch palette__swatch--grey"></div>
    <div class="palette__swatch palette__swatch--black"></div>
    <div class="palette__label">COLOR USE</div>
  </div>

  <section class="envelope">
    <div class="brand">
      <div class="brand__ring"></div>
      <div class="brand__name"><span>BRIGHTMOOR</span><span>dental care</span></div>
    </div>
    <address class="envelope__contact" style="font-style:normal">
      2180 S Brightmoor Ave Lakeview, XQ 00123-4567<br>
      555.014.2270<span class="divider">|</span>n.surname@brightmoordentalcarexq.example<br>
      brightmoordentalcarexq.example
    </address>
    <div class="stripe stripe--green"></div>
    <div class="stripe stripe--grey"></div>
  </section>

  <section class="card card--front">
    <div class="brand">
      <div class="brand__ring"></div>
      <div class="brand__name"><span>BRIGHTMOOR</span><span>dental care</span></div>
    </div>
    <div class="card__rule"></div>
    <div class="card__holder">
      <div class="card__name">Name Surname</div>
      <div class="card__role">Your Position</div>
    </div>
    <address class="card__contact" style="font-style:normal">
      2180 S Brightmoor Ave<br>
      Lakeview, XQ 00123-4567<br>
      555.014.2270<br>
      n.surname@brightmoordentalcarexq.example<br>
      brightmoordentalcarexq.example
    </address>
    <div class="card__watermark"></div>
    <div class="stripe stripe--green"></div>
    <div class="stripe stripe--grey"></div>
  </section>

  <section class="card card--back">
    <div class="brand">
      <div class="brand__ring"></div>
      <div class="brand__name"><span>BRIGHTMOOR</span><span>dental care</span></div>
    </div>
  </section>

  <div class="board-band"></div>
  <div class="board-label">STATIONERY DESIGN</div>
</body>
</html>
```